Facebook cover photo and Icon- Pet Related

I am looking to have a few custom cover photos designed for my business Facebook page so I can rotate between them every month.

We are a start up pet product delivery service for our local market. We specialize in dog and cat food and treats.

We want our Facebook page to have the same feel as our website to solidify our brand. Our work in progress website is www.hollowbarnrunners.com. Please not this is still a work in progress and some of the photos may be changing.

Each cover photo have a different look and feel however should still relate to our brand.

We would like 3 cover photos created with a 'theme' around each of the following phrases. Each saying should also be included on the photo itself.

1. You can't buy happiness, but you can buy local and that's kind of the same thing.
3. Sit. Stay. Let us fetch!
4. Making your life easier, theirs healthier and happier.

We are open to dog, cat, and people 'stock' photos being included as long as the photo goes with the saying.

In addition to the cover photos we would like a design for our 'profile photo' as well.

I am including our logos for you to use as needed.

Industry/Entity Type

Delivery Service

Requirements
Must have
• We would like the text over a photo of people with cats and dogs.
Nice to have
• If there is no photos of humans with cats and dogs the next best thing would be a graphic that goes with the text.
Should not have
• Not interested in designs with animated animals.

```html
<!DOCTYPE html>
<html lang="en">
<head>
<meta charset="utf-8">
<title>Hollow Barn Runners – Buy Local Cover</title>
<link rel="stylesheet" href="https://fonts.googleapis.com/css2?family=Nunito:wght@900&family=Sansita:ital,wght@1,800&family=Raleway:wght@400&display=swap">
<style>
  :root {
    --paper: #ffffff;
    --orange: #f28010;
    --red-orange: #f0601e;
    --aqua: #a6efe5;
    --grey: #b3b8bb;
    --yellow: #f4e41c;
    --lime: #96dc18;
    --brand-grey: #6f7173;
    --photo-dark: #6a6d73;
    --photo-mid: #a9a7a4;
    --photo-warm: #d2a06a;
  }
  html, body {
    margin: 0;
    padding: 0;
    overflow: hidden;
    background: var(--paper);
  }
  .cover {
    position: relative;
    width: 1200px;
    height: 601px;
    background: var(--paper);
    overflow: hidden;
  }
  .pets-photo {
    position: absolute;
    left: 45px;
    top: 165px;
    width: 545px;
    height: 380px;
    background: linear-gradient(90deg, var(--photo-dark) 0%, var(--photo-mid) 50%, var(--photo-warm) 75%, #efe4d6 100%);
    opacity: 0.85;
  }
  .slogan {
    margin: 0;
    font-size: inherit;
    font-weight: inherit;
  }
  .slogan span {
    position: absolute;
    line-height: 1;
    white-space: nowrap;
  }
  .rounded { font-family: "Nunito", "Arial Rounded MT Bold", sans-serif; font-weight: 900; }
  .light { font-family: "Raleway", "Century Gothic", sans-serif; font-weight: 400; }
  .script { font-family: "Sansita", Georgia, serif; font-weight: 800; font-style: italic; }

  .w-you { left: 185px; top: 40px; font-size: 92px; color: var(--orange); letter-spacing: -2px; }
  .w-cant { left: 388px; top: 70px; font-size: 54px; color: var(--aqua); }
  .w-buy-1 { left: 545px; top: 70px; font-size: 56px; color: var(--grey); }
  .w-happiness { left: 345px; top: 124px; font-size: 64px; color: var(--yellow); }
  .w-but { left: 472px; top: 194px; font-size: 56px; color: var(--red-orange); }
  .w-you-can { left: 583px; top: 198px; font-size: 48px; color: var(--aqua); }
  .w-buy-2 { left: 795px; top: 190px; font-size: 58px; color: var(--grey); }
  .w-local { left: 604px; top: 255px; font-size: 90px; color: var(--lime); }
  .w-and { left: 538px; top: 352px; font-size: 56px; color: var(--yellow); }
  .w-thats-kind { left: 668px; top: 352px; font-size: 56px; color: var(--red-orange); }
  .w-of-the { left: 652px; top: 420px; font-size: 52px; color: var(--grey); }
  .w-same-thing { left: 757px; top: 478px; font-size: 68px; color: var(--lime); }

  .brand {
    position: absolute;
    left: 1005px;
    top: 62px;
    width: 140px;
    text-align: center;
  }
  .brand-dot {
    display: block;
    width: 26px;
    height: 26px;
    margin: 0 auto 6px;
    border-radius: 50%;
    background: var(--brand-grey);
  }
  .brand-name {
    display: block;
    font-family: "Raleway", "Century Gothic", sans-serif;
    font-weight: 400;
    font-size: 19px;
    line-height: 1.05;
    color: var(--brand-grey);
  }
  .brand-tagline {
    display: block;
    margin-top: 4px;
    font-family: "Raleway", "Century Gothic", sans-serif;
    font-size: 6px;
    letter-spacing: 0.2px;
    color: var(--brand-grey);
  }
</style>
</head>
<body>
  <main class="cover">
    <div class="pets-photo" role="img" aria-label="Photo of a grey Weimaraner, a grey cat, a spaniel puppy and a pug looking upward"></div>

    <h1 class="slogan">
      <span class="rounded w-you">You</span>
      <span class="rounded w-cant">can’t</span>
      <span class="light w-buy-1">buy</span>
      <span class="script w-happiness">happiness,</span>
      <span class="light w-but">but</span>
      <span class="rounded w-you-can">you can</span>
      <span class="rounded w-buy-2">buy</span>
      <span class="script w-local">local</span>
      <span class="light w-and">and</span>
      <span class="light w-thats-kind">that’s kind</span>
      <span class="rounded w-of-the">of the</span>
      <span class="script w-same-thing">same thing.</span>
    </h1>

    <div class="brand">
      <span class="brand-dot"></span>
      <span class="brand-name">Hollow Barn Runners</span>
      <span class="brand-tagline">PREMIUM PET PRODUCTS DELIVERED</span>
    </div>
  </main>
</body>
</html>
```